We need a fresh, new church business card!!

We need a church business card with basic info to hand out as invites. We are looking for something clean that communicates our basic information clearly.

We are open to square or rectangle card sizes.

General Public

Religious

The attached logo is the only one that I have available. We'd like to see options with with text of the logo lighter and on a dark background as well as options with white/light backgrounds.

Also, we'd like to see option with rounded corners.

• Address - 2718 Maple Row, Lindenport, ST 00142
• Website - brookvane.example
• Phone - 555-555-0163
• Service times -
• Sunday - 10am Sunday School
• - 11am Family Worship
• - 6pm Night of Prayer
• Wednesday - 7:30pm Adult Bible Study
• Classes for all ages

```html
<!DOCTYPE html>
<html lang="en">
<head>
<meta charset="utf-8">
<title>Brookvane Pentecostal Church – Business Card</title>
<link href="https://fonts.googleapis.com/css2?family=Arimo:wght@400;700&display=swap" rel="stylesheet">
<style>
  :root {
    --teal: #3f8796;
    --teal-dark: #2f6f7d;
    --teal-light: #5ea3b1;
    --ink: #4a4a4a;
    --grey: #8a8a8a;
    --grey-block: #7d7d7d;
    --paper: #ffffff;
    --stage: #ecebe8;
  }
  * { box-sizing: border-box; margin: 0; padding: 0; }
  html, body { width: 1200px; height: 950px; overflow: hidden; }
  body {
    background: var(--stage);
    font-family: "Arimo", Arial, sans-serif;
    display: flex; flex-direction: column; align-items: center; justify-content: center;
    gap: 34px;
  }
  .card {
    width: 760px; height: 434px; position: relative; overflow: hidden;
    box-shadow: 0 6px 18px rgba(0,0,0,.18);
  }

  /* Back of card */
  .card--back {
    background: linear-gradient(135deg, var(--teal-dark) 0%, var(--teal) 55%, var(--teal-light) 100%);
    color: var(--paper);
    display: flex; flex-direction: column; align-items: center; justify-content: center;
    text-align: center;
  }
  .brand { display: flex; align-items: center; gap: 16px; }
  .brand__dot { width: 54px; height: 54px; border-radius: 50%; background: currentColor; flex: none; }
  .brand__name { font-weight: 700; font-size: 34px; letter-spacing: 1px; line-height: 1.05; text-align: left; }
  .brand__name span { display: block; font-size: 15px; letter-spacing: 3px; }
  .card--back .brand { margin-bottom: 34px; }
  .services { font-size: 18px; line-height: 1.45; }
  .services dt { font-weight: 700; }
  .services dd { margin-bottom: 10px; }
  .card--back .web { margin-top: 12px; font-size: 18px; letter-spacing: 3px; font-weight: 700; }

  /* Front of card */
  .card--front { background: linear-gradient(160deg, #fff 0%, #f3f3f3 100%); color: var(--ink); }
  .card--front .brand { position: absolute; left: 60px; top: 124px; color: var(--grey); }
  .card--front .brand__name { font-size: 30px; }
  .card--front .brand__name span { font-size: 13px; }
  .divider { position: absolute; left: 400px; top: 70px; width: 1px; height: 230px;
    background: linear-gradient(180deg, transparent, #b8b8b8 30%, #b8b8b8 70%, transparent); }
  .contact { position: absolute; left: 432px; top: 88px; font-size: 19px; line-height: 1.35; }
  .contact__name { color: var(--teal); font-weight: 700; font-size: 23px; }
  .contact__role { color: var(--grey); margin-bottom: 14px; }
  .contact__line { display: flex; align-items: center; gap: 8px; }
  .contact__line svg { width: 18px; height: 18px; fill: var(--teal); flex: none; }
  .band { position: absolute; left: 0; right: 0; bottom: 0; height: 86px; display: flex; }
  .band__stripe { position: absolute; left: 0; right: 0; top: -10px; height: 6px; background: var(--teal-light); opacity: .7; }
  .band__main { flex: 1; background: linear-gradient(90deg, var(--teal) 0%, var(--teal-dark) 100%);
    color: var(--paper); display: flex; align-items: center; padding-left: 60px;
    font-size: 20px; letter-spacing: 4px; }
  .band__end { width: 130px; background: var(--grey-block); display: flex; align-items: center; justify-content: center; }
  .band__end .brand__dot { width: 30px; height: 30px; background: var(--paper); }
</style>
</head>
<body>

<section class="card card--back" aria-label="Card back">
  <div class="brand">
    <div class="brand__dot"></div>
    <div class="brand__name">BROOKVANE<span>PENTECOSTAL CHURCH</span></div>
  </div>
  <dl class="services">
    <dt>Sunday</dt>
    <dd>10am Sunday School, 11am Family Worship, 6pm Night of Prayer</dd>
    <dt>Wednesday</dt>
    <dd>7:30pm Adult Bible Study, Classes for all ages</dd>
  </dl>
  <p class="web">www.brookvane.example</p>
</section>

<section class="card card--front" aria-label="Card front">
  <div class="brand">
    <div class="brand__dot"></div>
    <div class="brand__name">BROOKVANE<span>PENTECOSTAL CHURCH</span></div>
  </div>
  <div class="divider"></div>
  <div class="contact">
    <p class="contact__name">Mark Ellison</p>
    <p class="contact__role">President</p>
    <p>2718 Maple Row,</p>
    <p>Lindenport, ST 00142</p>
    <p class="contact__line">
      <svg viewBox="0 0 24 24" aria-hidden="true"><path d="M6.6 10.8a15.1 15.1 0 0 0 6.6 6.6l2.2-2.2a1 1 0 0 1 1-.25 11.4 11.4 0 0 0 3.6.57 1 1 0 0 1 1 1V20a1 1 0 0 1-1 1A17 17 0 0 1 3 4a1 1 0 0 1 1-1h3.5a1 1 0 0 1 1 1c0 1.250.2 2.450.57 3.57a1 1 0 0 1-.25 1z"/></svg>
      555-555-0163
    </p>
    <p class="contact__line">
      <svg viewBox="0 0 24 24" aria-hidden="true"><path d="M2 5h20v14H2z M2 5l10 8 10-8" fill="none" stroke="#3f8796" stroke-width="2"/><path d="M3 6h18l-9 7z"/></svg>
      info@brookvane.example
    </p>
  </div>
  <div class="band">
    <div class="band__stripe"></div>
    <div class="band__main">www.brookvane.example</div>
    <div class="band__end"><div class="brand__dot"></div></div>
  </div>
</section>

</body>
</html>
```